Realty Group Needs Classy, Contemporary Letterhead Design

We need a letterhead design for a new realty company located in NY, USA. We buy investment properties to rehabilitate and or keep in our rental portfolio.

```html
<!DOCTYPE html>
<html lang="en">
<head>
<meta charset="utf-8">
<title>Meridian Realty Group Letterhead</title>
<link href="https://fonts.googleapis.com/css2?family=Source+Sans+3:wght@400;600;700&family=Quicksand:wght@400&display=swap" rel="stylesheet">
<style>
  :root {
    --backdrop: #ebebed;
    --paper: #ffffff;
    --brand-purple: #4e2d84;
    --ink: #555558;
    --ink-soft: #6b6b6e;
    --icon-gray: #8a8a8c;
    --band-gray: #a5a5a7;
  }
  * { margin: 0; padding: 0; box-sizing: border-box; }
  html, body { width: 1200px; height: 1200px; overflow: hidden; background: var(--backdrop); }
  .letterhead {
    position: absolute; left: 197px; top: 35px; width: 806px; height: 1130px;
    background: var(--paper); overflow: hidden;
    font-family: "Source Sans 3", "Myriad Pro", sans-serif; color: var(--ink);
  }
  .brand { position: absolute; left: 86px; top: 72px; display: flex; align-items: center; gap: 10px; }
  .brand-mark { width: 16px; height: 16px; background: var(--brand-purple); }
  .brand-name { font-size: 27px; font-weight: 700; color: var(--brand-purple); line-height: 1; }
  .contact-block { position: absolute; right: 90px; top: 50px; }
  .contact-row { display: flex; align-items: center; justify-content: flex-end; gap: 14px; margin-bottom: 10px; height: 26px; }
  .contact-text { font-family: "Quicksand", sans-serif; font-size: 11.5px; line-height: 14px; text-align: right; color: var(--ink-soft); letter-spacing: 0.3px; }
  .contact-icon { width: 23px; height: 23px; display: flex; align-items: center; justify-content: center; background: var(--icon-gray); }
  .contact-icon.is-brand { background: var(--brand-purple); }
  .recipient { position: absolute; left: 88px; top: 253px; }
  .recipient-name { font-size: 14.5px; line-height: 18px; }
  .recipient-title { font-size: 11px; line-height: 14px; margin: 3px 0 7px; }
  .recipient-line { font-size: 13.5px; line-height: 23px; }
  .recipient-line b { font-weight: 600; display: inline-block; width: 24px; }
  .letter-date { position: absolute; right: 93px; top: 340px; font-size: 13.5px; }
  .letter-body { position: absolute; left: 88px; top: 424px; width: 650px; font-size: 14.6px; line-height: 30px; color: var(--ink-soft); white-space: nowrap; }
  .letter-body p { margin-bottom: 31px; }
  .signature { position: absolute; left: 88px; top: 983px; }
  .signature-name { font-size: 14.5px; font-weight: 700; line-height: 18px; }
  .signature-role { font-size: 13px; line-height: 16px; }
  .footer-band {
    position: absolute; left: 110px; bottom: 0; width: 590px; height: 32px;
    background: linear-gradient(90deg, var(--band-gray) 0%, var(--brand-purple) 22%, var(--brand-purple) 78%, var(--band-gray) 100%);
  }
</style>
</head>
<body>
  <main class="letterhead">
    <header>
      <div class="brand">
        <span class="brand-mark"></span>
        <span class="brand-name">Meridian Realty Group, LLC</span>
      </div>
      <div class="contact-block">
        <div class="contact-row">
          <div class="contact-text">+1 212 555 0190<br>+1 212 555 0191</div>
          <div class="contact-icon">
            <svg width="13" height="13" viewBox="0 0 24 24"><path fill="#fff" d="M6.6 10.8a15 15 0 0 0 6.6 6.6l2.2-2.2c.3-.3.7-.4 1-.2 1.1.4 2.3.6 3.6.6.6 0 1 .4 1 1V20c0 .6-.4 1-1 1A17 17 0 0 1 3 4c0-.6.4-1 1-1h3.5c.6 0 1 .4 1 1 0 1.3.2 2.5.6 3.6.1.3 0 .7-.2 1z"/></svg>
          </div>
        </div>
        <div class="contact-row">
          <div class="contact-text">meridianrealty.com<br>info@meridianrealty.com</div>
          <div class="contact-icon is-brand">
            <svg width="13" height="13" viewBox="0 0 24 24" fill="none" stroke="#fff" stroke-width="2"><circle cx="12" cy="12" r="9"/><path d="M3 12h18M12 3c3 3 3 15 0 18M12 3c-3 3-3 15 0 18"/></svg>
          </div>
        </div>
        <div class="contact-row">
          <div class="contact-text">48 Linden Street<br>NY, USA</div>
          <div class="contact-icon">
            <svg width="12" height="14" viewBox="0 0 24 28"><path fill="#fff" d="M12 1a9 9 0 0 0-9 9c0 7 9 17 9 17s9-10 9-17a9 9 0 0 0-9-9zm0 12.5a3.5 3.5 0 1 1 0-7 3.5 3.5 0 0 1 0 7z"/></svg>
          </div>
        </div>
      </div>
    </header>

    <section class="recipient">
      <div class="recipient-name">Owen Hale</div>
      <div class="recipient-title">Chief Director</div>
      <div class="recipient-line"><b>A :</b>22-4, Harbor Lane Brooklyn - 1120</div>
      <div class="recipient-line"><b>W :</b>owen@hallmail.com, www.halldesk.com</div>
      <div class="recipient-line"><b>P :</b>+1 - 212 - 555 - 0147</div>
    </section>
    <div class="letter-date">Date, 10 September, 2019</div>

    <article class="letter-body">
      <p>This is a sample letter that has been placed to demonstrate typing remat (Your Company). letterhead<br>design. When positioned properly, it will serve to work in harmony with all other elements letterhead.<br>This letterhead design is meant to project an image</p>
      <p>This letterhead design is meant project an image of professionalism reliability. By using simple aligen<br>we have created a very spacious feeling. The simplicity suggest rengththe spaciousnes contributes h<br>aesthetics the layout. These basic qualities along with the (Your Company)</p>
      <p>look and helps reinforce the (Your Company) brand. letterhead design is meant to project an image p<br>design. When positioned properly, it will serve to work in harmony all the other elements letterhead.<br>sionalism and reliability.</p>
      <p>This letterhead design is based on the (Form of your logo) form (Your Company) logo. Each stationery<br>we have created a very spacious feeling. The simplicity suggests strength the spaciousnes contribute<br>part of the (Form of your logo).</p>
    </article>

    <footer class="signature">
      <div class="signature-name">Clara Voss</div>
      <div class="signature-role">Manager</div>
    </footer>

    <div class="footer-band" role="img" aria-label="Decorative footer band in gray and purple"></div>
  </main>
</body>
</html>
```